Label design, for stand up guayusa tea pouch.

I need a high quality, clean, modern sticker label design. Its going on a stand up tea pouch. The front of the pouch is transparent, with a foil back. The foil back is visible from front view.The product is a dark green herb. its in the form of loose leaf tea. Guayusa provides clean energy. Its main point is that its an alternative to coffee with similar caffeine levels, but it doesn't give the same jittery feeling as coffee because of a component called theobromine.

Target Market(s)

Men and women 18-65

Font styles to use
Sans Serif
Decorative

Colors

Designer to choose colors to be used in the design.

Requirements
Must have
• -Logo provided: icon
• The logo icon colors can be changed to have some green if it will work better
• -Brand: Lanternpeak guayusa
• -A background that goes well with the packaging (transparent/foil) picture provided
Should not have
• Blank background
• Overly loud background

```html
<!DOCTYPE html>
<html lang="en">
<head>
<meta charset="utf-8">
<title>Lanternpeak Guayusa – Pouch Label</title>
<link rel="stylesheet" href="https://fonts.googleapis.com/css2?family=Alfa+Slab+One&family=Lora:ital,wght@0,700;1,400&family=Open+Sans:wght@600;700&display=swap">
<style>
  :root {
    --backdrop: #ebebeb;
    --label-cream: #fdf4c6;
    --leaf-green: #72ad2d;
    --ink: #1f1f1f;
    --pill-text: #f6f9e8;
  }
  * { margin: 0; padding: 0; box-sizing: border-box; }
  html, body { width: 1200px; height: 1093px; overflow: hidden; }
  body { background: var(--backdrop); position: relative; }

  .label {
    position: absolute; left: 280px; top: 80px;
    width: 640px; height: 930px;
    background: var(--label-cream);
    border-radius: 56px;
    box-shadow: 0 6px 18px rgba(0,0,0,0.12);
  }
  .label__frame {
    position: absolute; left: 32px; top: 48px; right: 32px; bottom: 58px;
    border: 3px solid var(--leaf-green);
    border-radius: 44px;
    display: flex; flex-direction: column; align-items: center;
    color: var(--ink);
  }
  .brand { margin-top: 70px; display: flex; flex-direction: column; align-items: center; gap: 14px; }
  .brand__dot { width: 76px; height: 76px; border-radius: 50%; background: var(--leaf-green); }
  .brand__name {
    font-family: "Open Sans", sans-serif; font-weight: 700;
    font-size: 25px; color: var(--leaf-green);
  }
  .product-title {
    margin-top: 38px;
    font-family: "Alfa Slab One", serif;
    font-size: 84px; letter-spacing: 3px; line-height: 1;
    color: var(--ink);
  }
  .product-subtitle {
    margin-top: 14px;
    font-family: "Lora", serif; font-style: italic;
    font-size: 23px; letter-spacing: 0.5px;
  }
  .product-description {
    margin-top: 22px; width: 440px; text-align: center;
    font-family: "Lora", serif; font-weight: 700;
    font-size: 18px; line-height: 1.3;
  }
  .divider { width: 100%; height: 3px; background: var(--leaf-green); }
  .divider--top { margin-top: 40px; }
  .preparation {
    padding: 18px 30px;
    font-family: "Lora", serif; font-style: italic;
    font-size: 15px; line-height: 1.4; text-align: justify;
  }
  .energy-pill {
    margin-top: 32px;
    width: 300px; height: 74px; border-radius: 37px;
    background: var(--leaf-green); color: var(--pill-text);
    display: flex; flex-direction: column; justify-content: center; align-items: center;
    font-family: "Open Sans", sans-serif; font-weight: 600;
    font-size: 16px; line-height: 1.35; letter-spacing: 0.8px;
  }
  .net-weight {
    margin-top: 26px;
    font-family: "Lora", serif; font-style: italic; font-size: 21px;
  }
</style>
</head>
<body>
  <div class="label">
    <div class="label__frame">
      <div class="brand">
        <div class="brand__dot"></div>
        <div class="brand__name">Lanternpeak tea</div>
      </div>
      <h1 class="product-title">GUAYUSA</h1>
      <p class="product-subtitle">ENERGIZING HERBAL TEA</p>
      <p class="product-description">Guayusa is made from holly leaves grown in the Amazon. It is an excellent source of antioxidants and vitamins.</p>
      <div class="divider divider--top"></div>
      <p class="preparation">To prepare, cold water should be boiled and then poured onto the leaves. The leaves should be allowed to steep in the water for at least four minutes for weak tea. For every 8 ounces (236 ml) of water, 2 grams of tea leaves are suggested.</p>
      <div class="divider"></div>
      <div class="energy-pill">
        <span>PROVIDES CLEAN ENERGY</span>
        <span>CONTENT THEOBROMINE</span>
      </div>
      <p class="net-weight">XXX gr</p>
    </div>
  </div>
</body>
</html>
```